Water Well Drilling

Banner will be 2m wide X 4m high. The Banner will be placed on side of road. The application of the banner is for advertising of our water well drilling services. The banner must be designed using two different languages. English and Spanish. The design would be in accordance with our website and Logo designs to maintain the same marketing image. Website www.brisacanyondrilling.com

```html
<!DOCTYPE html>
<html lang="en">
<head>
<meta charset="utf-8">
<title>Water Well Drilling – Roadside Banner</title>
<link href="https://fonts.googleapis.com/css2?family=Montserrat:wght@600;700;800&display=swap" rel="stylesheet">
<style>
  :root {
    --page-bg: #e9eaec;
    --navy: #2b355e;
    --navy-deep: #141a33;
    --brand-blue: #1d4a8a;
    --white: #ffffff;
  }
  html, body {
    margin: 0;
    padding: 0;
    width: 1200px;
    height: 1171px;
    overflow: hidden;
    background: var(--page-bg);
    font-family: "Montserrat", Arial, sans-serif;
  }
  .banner {
    position: absolute;
    left: 322px;
    top: 30px;
    width: 556px;
    height: 1111px;
    display: flex;
    flex-direction: column;
    background: var(--white);
    box-shadow: 0 4px 18px rgba(0,0,0,0.18);
  }
  .section-english {
    height: 463px;
    background: linear-gradient(180deg, var(--navy) 0%, #262f55 70%, var(--navy-deep) 100%);
    color: var(--white);
    padding: 44px 0 0 62px;
    box-sizing: border-box;
  }
  .headline {
    margin: 0;
    font-weight: 800;
    font-size: 64px;
    line-height: 1.0;
    letter-spacing: 1px;
  }
  .headline span { display: block; margin-bottom: 8px; }
  .services {
    list-style: none;
    margin: 44px 0 0 -30px;
    padding: 0;
    font-weight: 700;
    font-size: 24px;
    letter-spacing: 0.3px;
  }
  .services li {
    display: flex;
    align-items: flex-start;
    margin-bottom: 22px;
    line-height: 1.25;
  }
  .services li::before {
    content: "";
    flex: none;
    width: 11px;
    height: 11px;
    background: var(--white);
    margin: 8px 14px 0 0;
  }
  .brand-band {
    height: 96px;
    display: flex;
    align-items: center;
    justify-content: center;
    gap: 12px;
    border-bottom: 4px solid var(--brand-blue);
  }
  .brand-dot {
    width: 22px;
    height: 22px;
    border-radius: 50%;
    background: var(--brand-blue);
  }
  .brand-name {
    color: var(--brand-blue);
    font-weight: 700;
    font-size: 23px;
    letter-spacing: 0.5px;
  }
  .contact-band {
    height: 140px;
    display: flex;
    flex-direction: column;
    align-items: center;
    justify-content: center;
    gap: 14px;
    color: var(--brand-blue);
  }
  .phone {
    display: flex;
    align-items: center;
    gap: 14px;
    font-weight: 800;
    font-size: 46px;
    letter-spacing: 2px;
  }
  .phone svg { width: 58px; height: 58px; }
  .email {
    display: flex;
    align-items: center;
    gap: 12px;
    font-weight: 700;
    font-size: 20px;
  }
  .email svg { width: 26px; height: 18px; }
  .section-spanish {
    height: 330px;
    background: linear-gradient(180deg, var(--navy-deep) 0%, #232c52 40%, var(--navy-deep) 100%);
    color: var(--white);
    padding: 32px 0 0 72px;
    box-sizing: border-box;
  }
  .section-spanish .headline { font-size: 54px; }
  .section-spanish .headline span { margin-bottom: 10px; }
  .section-spanish .services { margin-top: 14px; font-size: 23px; }
  .section-spanish .services li { margin-bottom: 16px; }
  .bottom-band {
    flex: 1;
    display: flex;
    align-items: center;
    justify-content: center;
    color: var(--brand-blue);
  }
  .bottom-band .phone { font-size: 42px; }
  .bottom-band .phone svg { width: 52px; height: 52px; }
</style>
</head>
<body>
  <main class="banner">
    <section class="section-english">
      <h1 class="headline"><span>WATER</span><span>WELL</span><span>DRILLING</span></h1>
      <ul class="services">
        <li>PERMITS AND CONCESSIONS</li>
        <li>PUMP INSTALL AND REPAIR</li>
      </ul>
    </section>

    <div class="brand-band">
      <span class="brand-dot"></span>
      <span class="brand-name">Perforaciones Brisa Cañón</span>
    </div>

    <div class="contact-band">
      <div class="phone">
        <svg viewBox="0 0 60 60" aria-hidden="true">
          <circle cx="30" cy="30" r="26" fill="none" stroke="currentColor" stroke-width="5"/>
          <path d="M21 16c2-1 4 0 5 2l2 5c1 2 0 3-1 4l-2 2c1 4 4 7 8 9l2-2c1-1 3-2 4-1l5 2c2 1 3 3 2 5l-1 3c-1 2-3 3-6 2-11-3-18-10-21-21-1-3 0-5 3-6z" fill="currentColor"/>
        </svg>
        <span>8614 2093</span>
      </div>
      <div class="email">
        <svg viewBox="0 0 26 18" aria-hidden="true">
          <rect x="1" y="1" width="24" height="16" fill="none" stroke="currentColor" stroke-width="2"/>
          <path d="M1 1l12 9 12-9" fill="none" stroke="currentColor" stroke-width="2"/>
        </svg>
        <span>Info@brisacanyondrilling.com</span>
      </div>
    </div>

    <section class="section-spanish" lang="es">
      <h2 class="headline"><span>PERFORACIÓN</span><span>DE POZOS</span></h2>
      <ul class="services">
        <li>PERMISOS Y CONCESIONES</li>
        <li>INSTALACIÓN Y REPARACIÓN<br>DE BOMBAS</li>
      </ul>
    </section>

    <div class="bottom-band">
      <div class="phone">
        <svg viewBox="0 0 60 60" aria-hidden="true">
          <circle cx="30" cy="30" r="26" fill="none" stroke="currentColor" stroke-width="5"/>
          <path d="M21 16c2-1 4 0 5 2l2 5c1 2 0 3-1 4l-2 2c1 4 4 7 8 9l2-2c1-1 3-2 4-1l5 2c2 1 3 3 2 5l-1 3c-1 2-3 3-6 2-11-3-18-10-21-21-1-3 0-5 3-6z" fill="currentColor"/>
        </svg>
        <span>88207461</span>
      </div>
    </div>
  </main>
</body>
</html>
```